Brantley Advisory Group provides support for renewable energy projects to utilities and suppliers

I need a professional looking business card that is both simple and elegant and unique. My clients are mostly large organizations not individuals. I am a consultant with my own company that is small but would like to give clients the impression I am larger. Smart grid, fiber optics, software, field hardware, distribution automation, substation automation, operations, energy storage/batteries, microgrids, customer service, strategy/roadmaps, conservation, Automated Metering Infrastruture (AMI or smart meters) are all areas of focus.

Target Market(s)

Utilities, suppliers, governmental agencies involved in energy. All types of energy especially natural gas and electrical. Especially renewable energy or green projects.

Contact Information for Business Card

Name - Mark Brantley Cell Phone - 425.318.2746 Email - mbrantley@brantleyag-example.com
Company - Brantley Advisory Group (logo) Title - Principal

Font styles to use
Serif
Sans Serif

Colors

Designer to choose colors to be used in the design.

Requirements
Must have
• Simple and professional and powerful.
• Unique/creative design.
Nice to have
• Utilize color scheme to accent logo colors. Maybe some geometric pattern on edge of card with color.
Should not have
• Busy, complicated, traditional

```html
<!DOCTYPE html>
<html lang="en">
<head>
<meta charset="utf-8">
<title>Brantley Advisory Group – Business Card</title>
<link rel="stylesheet" href="https://fonts.googleapis.com/css2?family=Dosis:wght@700&family=Tinos&display=swap">
<style>
  :root {
    --backdrop: #02005f;
    --card-front: #e5e5e5;
    --card-back: #ffffff;
    --brand-indigo: #2409a3;
    --brand-green: #66903d;
    --band-grey: #e5e5e5;
    --accent-frame: #dddddd;
    --ink: #111111;
    --rule: #666666;
  }
  * { margin: 0; padding: 0; box-sizing: border-box; }
  html, body { width: 1200px; height: 1200px; overflow: hidden; }
  body { background: var(--backdrop); position: relative; }

  .card { position: absolute; left: 230px; width: 739px; height: 450px; overflow: hidden; }
  .card--front { top: 127px; background: var(--card-front); }
  .card--back { top: 622px; background: var(--card-back); }

  .brand { position: absolute; display: flex; align-items: center; z-index: 1; }
  .brand__mark { border: 5px solid var(--brand-green); border-radius: 6px; flex: none; }
  .brand__name {
    font-family: "Dosis", sans-serif; font-weight: 700;
    color: var(--brand-indigo); line-height: 1.05;
  }

  .card--front .brand { left: 112px; top: 165px; gap: 34px; }
  .card--front .brand__mark { width: 90px; height: 90px; }
  .card--front .brand__name { font-size: 50px; }

  .card--back .brand { left: 53px; top: 58px; gap: 24px; }
  .card--back .brand__mark { width: 62px; height: 62px; border-width: 4px; }
  .card--back .brand__name { font-size: 34px; }

  .accent-frame {
    position: absolute; left: 532px; top: 21px; width: 188px; height: 188px;
    border: 11px solid var(--accent-frame); border-radius: 16px; z-index: 0;
  }

  .holder {
    position: absolute; left: 80px; top: 270px; z-index: 1;
    font-family: "Tinos", serif; font-size: 40px; color: var(--ink);
  }

  .contact-rule {
    position: absolute; left: 358px; top: 254px; width: 2px; height: 143px;
    background: var(--rule); z-index: 1;
  }
  .contact {
    position: absolute; left: 378px; top: 244px; list-style: none; z-index: 1;
    font-family: "Tinos", serif; font-size: 20px; color: var(--ink);
  }
  .contact li { display: flex; align-items: center; height: 30px; white-space: nowrap; }
  .contact__icon { width: 20px; height: 20px; margin-right: 20px; flex: none; }
  .contact__icon--blank { visibility: hidden; }

  .edge-bands { position: absolute; left: 0; top: 415px; z-index: 1; }
</style>
</head>
<body>
  <section class="card card--front">
    <div class="brand">
      <span class="brand__mark"></span>
      <span class="brand__name">Brantley<br>Advisory Group</span>
    </div>
  </section>

  <section class="card card--back">
    <div class="accent-frame"></div>

    <div class="brand">
      <span class="brand__mark"></span>
      <span class="brand__name">Brantley<br>Advisory Group</span>
    </div>

    <p class="holder">Mark Brantley</p>

    <div class="contact-rule"></div>
    <ul class="contact">
      <li>
        <svg class="contact__icon" viewBox="0 0 24 24"><path d="M12 2a7 7 0 0 0-7 7c0 5 7 12 7 12s7-7 7-12a7 7 0 0 0-7-7z" fill="#111"/><circle cx="12" cy="9" r="2.6" fill="#fff"/></svg>
        Your Adress
      </li>
      <li>
        <svg class="contact__icon contact__icon--blank" viewBox="0 0 24 24"></svg>
        Your Adress
      </li>
      <li>
        <svg class="contact__icon" viewBox="0 0 24 24"><rect x="6" y="3" width="11" height="19" rx="2" fill="none" stroke="#111" stroke-width="2"/><circle cx="11.5" cy="18.5" r="1.2" fill="#111"/></svg>
        425.318.2746
      </li>
      <li>
        <svg class="contact__icon" viewBox="0 0 24 24" fill="none" stroke="#111" stroke-width="1.4"><circle cx="12" cy="12" r="9"/><ellipse cx="12" cy="12" rx="4" ry="9"/><path d="M3 12h18M4.5 7.5h15M4.5 16.5h15"/></svg>
        www.yoursite.com
      </li>
      <li>
        <svg class="contact__icon" viewBox="0 0 24 24"><rect x="3" y="6" width="18" height="12" fill="#111"/><path d="M3 6l9 7 9-7" fill="none" stroke="#fff" stroke-width="1.5"/></svg>
        mbrantley@brantleyag-example.com
      </li>
    </ul>

    <svg class="edge-bands" width="739" height="35" viewBox="0 0 739 35">
      <polygon points="0,12 444,12 462,35 0,35" fill="var(--band-grey)"/>
      <polygon points="450,5 739,5 739,28 465,28" fill="var(--brand-green)"/>
    </svg>
  </section>
</body>
</html>
```